Design mobile friendly real estate and property management company landing page

Design a clean, crisp modern looking landing page that is mobile-friendly (must resize, preferably using bootstrap framework). Landing page will consist of heading with login area, company info, body consists of company description and services, a list of available rental properties with photos, and a footer with additional links and info. Working on updating with text for text areas marked A, B, and C on the layout pdf, but in meantime, lorem ipsum is fine. I can connect events to most buttons, etc. Just need the bootstrap and html functionality set up. Previous company website (which should not be relied upon) is www.kbtq.net This is somewhat of a template for a start, but looking for a more professional and modern design for the new website. But this gives an idea of the content and what needs to be displayed, and how.

Target Market(s)

Clients looking for a property management company that is efficient and well-organized.

Industry/Entity Type

Property Management

Coding

Coded - Design and coding required

Number of Pages Required

1 page

Font styles to use
Sans Serif

Colors
0355a3

Requirements
Must have
• Resize for the screen using bootstrap.
• Navigation that collapses for mobile devices
• Large text boxes and good solid spacing around all elements.
Nice to have
• for property images it would be nice if they can be swiped on touch enabled devices (to the next or previous image). And have navigation that can be clicked to next or previous images.
• Would be nice if a captcha verification was included on contact form.
Should not have
• Fancy or eccentric art

```html
<!DOCTYPE html>
<html lang="en">
<head>
<meta charset="utf-8">
<title>Northgate Realty</title>
<link href="https://fonts.googleapis.com/css2?family=Raleway:wght@300;400;600;700&family=Open+Sans:wght@400;600;700&family=Roboto+Condensed:wght@400;700&display=swap" rel="stylesheet">
<style>
:root{
  --blue:#0355a3;
  --ink:#333;
  --muted:#666;
  --line:#d5d5d5;
  --pale:#efefef;
  --dark:#1e1e1e;
  --darker:#141414;
  --white:#fff;
}
*{box-sizing:border-box;margin:0;padding:0}
html,body{width:1200px;height:2857px;overflow:hidden}
body{font-family:'Open Sans',sans-serif;color:var(--ink);background:var(--white);position:relative}
section,header{overflow:hidden}
.wrap{width:880px;margin:0 auto;position:relative}

/* hero */
.hero{position:relative;height:663px;background:linear-gradient(160deg,#3a2a1e 0%,#6b4a30 35%,#8a6a48 55%,#4a3424 80%,#2c1e14 100%);color:var(--white)}
.hero-photo{position:absolute;inset:0}
.topbar{position:absolute;top:0;left:0;right:0;height:38px;border-bottom:1px solid rgba(255,255,255,.15);background:rgba(0,0,0,.25)}
.topbar .wrap{display:flex;align-items:center;height:38px;font-size:11px}
.topbar .contact{display:flex;align-items:center;margin-right:34px}
.topbar .ic{width:20px;height:20px;border-radius:50%;background:var(--white);display:inline-flex;align-items:center;justify-content:center;margin-right:9px}
.social{margin-left:auto;display:flex;gap:7px}
.social span{width:21px;height:21px;border:1px solid rgba(255,255,255,.8);border-radius:50%}
.nav{position:absolute;top:38px;left:0;right:0}
.nav .wrap{display:flex;align-items:center;height:66px}
.brand{font-family:'Raleway',sans-serif;font-weight:600;font-size:19px;letter-spacing:1px;color:var(--white)}
.menu{margin-left:auto;display:flex;gap:37px;font-size:10px;font-weight:600;letter-spacing:.3px}
.menu a{color:var(--white);text-decoration:none;padding-bottom:5px}
.menu a.active{border-bottom:1px solid var(--white)}
.hero-copy{position:absolute;top:285px;left:0;right:0;text-align:center}
.hero-copy h1{font-family:'Raleway',sans-serif;font-weight:700;font-size:58px;letter-spacing:1px}
.hero-copy p{font-family:'Raleway',sans-serif;font-size:26px;line-height:31px;margin-top:12px}
.arrow{position:absolute;top:320px;width:72px;height:52px;background:rgba(0,0,0,.35);display:flex;align-items:center;justify-content:center}
.arrow.prev{left:0}.arrow.next{right:0}
.dots{position:absolute;top:622px;left:0;right:0;display:flex;justify-content:center;gap:6px}
.dots span{width:20px;height:3px;background:rgba(255,255,255,.45)}
.dots span.on{background:var(--white)}

/* search */
.search{height:189px;background:var(--pale);padding-top:36px}
.search .grid{display:grid;grid-template-columns:repeat(4,200px);column-gap:26px;row-gap:12px}
.field label{display:block;font-size:10px;text-transform:uppercase;color:#555;margin-bottom:8px}
.field .box{height:30px;background:var(--white);border:1px solid var(--line);font-size:10px;color:#555;display:flex;align-items:center;justify-content:space-between;padding:0 10px}
.btn-search{margin-top:17px;height:30px;background:var(--blue);color:var(--white);font-size:10px;text-transform:uppercase;display:flex;align-items:center;justify-content:center;font-weight:600}

/* section titles */
.title{text-align:center;font-family:'Raleway',sans-serif;font-size:28px;line-height:34px;font-weight:300;color:#555;letter-spacing:.5px}
.title b{font-weight:700;color:var(--blue)}
.rule{position:relative;width:220px;height:9px;margin:12px auto 0}
.rule::before{content:"";position:absolute;left:0;right:0;top:4px;height:1px;background:var(--blue)}
.rule::after{content:"";position:absolute;left:106px;top:0;width:9px;height:9px;border-radius:50%;background:var(--blue)}

/* about */
.about{padding-top:28px;height:443px}
.about-body{display:flex;margin-top:37px}
.collage{position:relative;width:345px;height:303px;flex:none}
.collage div{position:absolute;border:3px solid var(--white);box-shadow:0 1px 4px rgba(0,0,0,.3)}
.about-text{margin-left:107px;width:428px;font-size:11.5px;line-height:18.5px;color:#444}
.checks{list-style:none;margin-top:42px}
.checks li{display:flex;align-items:center;gap:14px;line-height:18px}

/* services */
.services{height:435px;padding-top:27px}
.svc-row{display:grid;grid-template-columns:repeat(4,220px);margin-top:12px;text-align:center}
.svc svg{display:block;margin:0 auto}
.svc h3{font-size:13px;font-weight:400;text-transform:uppercase;color:#333;margin-top:16px}
.svc p{font-size:11px;line-height:17px;color:#555;margin:10px auto 0;width:190px}
.svc .more{display:inline-block;margin-top:20px;font-size:10px;color:var(--blue);text-transform:uppercase}

/* testimonial */
.clients{height:343px;background:linear-gradient(180deg,#2c2c2c,#3a3936 50%,#262524);color:var(--white);text-align:center;padding-top:42px;position:relative}
.clients .title{color:#ddd}
.clients .title b{color:var(--white)}
.clients .rule::before{background:rgba(255,255,255,.7)}
.clients .rule::after{background:var(--white)}
.quote{font-size:12px;line-height:22px;margin-top:34px}
.person{display:flex;align-items:center;justify-content:center;gap:18px;margin-top:30px;margin-left:-30px}
.avatar{width:76px;height:76px;border-radius:50%;border:3px solid var(--white);background:linear-gradient(160deg,#e4c9a5,#b08a66)}
.person div{text-align:left;font-size:12px}
.person em{display:block;font-size:10px;margin-top:2px}

/* properties */
.props{padding-top:38px;height:512px}
.cards{display:grid;grid-template-columns:repeat(3,278px);column-gap:23px;margin-top:19px}
.card{border:1px solid #e2e2e2;background:var(--white);position:relative;height:336px;display:flex;flex-direction:column}
.card.lift{box-shadow:0 6px 18px rgba(0,0,0,.25)}
.card .photo{height:164px;position:relative;flex:none}
.price{position:absolute;top:8px;left:8px;background:var(--blue);color:var(--white);font-size:12px;padding:4px 8px}
.card .info{padding:10px 10px 0;flex:1}
.card h4{font-family:'Roboto Condensed',sans-serif;font-size:16px;font-weight:700;color:#222}
.card .tag{font-size:9px;color:var(--blue);margin-top:4px}
.card p{font-size:10px;line-height:16px;color:#555;margin-top:10px}
.card .meta{display:flex;align-items:center;background:#eee;height:25px;padding:0 10px;font-size:10px;color:#555;gap:6px;flex:none}
.card .meta .r{margin-left:auto;display:flex;gap:18px}

/* footer */
.footer{position:absolute;left:0;right:0;top:2585px;height:215px;background:var(--dark);color:#ddd}
.footer .wrap{display:grid;grid-template-columns:225px 226px 225px 204px;padding-top:27px;font-size:10.5px;line-height:15px}
.footer h5{font-size:11px;font-weight:700;color:var(--white);text-transform:uppercase;margin-bottom:22px;letter-spacing:.3px}
.footer .brand{font-size:14px;margin-bottom:22px}
.fcontact div{display:flex;align-items:center;gap:10px;margin-bottom:18px}
.fcontact .ci{width:20px;height:20px;border-radius:50%;background:var(--white);flex:none;display:flex;align-items:center;justify-content:center}
.links{list-style:none}
.links li{margin-bottom:8px;padding-left:16px;position:relative;font-size:10px}
.links li::before{content:"";position:absolute;left:0;top:6px;width:4px;height:4px;border-radius:50%;background:var(--white)}
.news-form{display:flex;margin-top:38px}
.news-form .in{width:168px;height:30px;background:var(--white);color:#777;font-size:9px;display:flex;align-items:center;padding-left:8px}
.news-form .go{width:36px;height:30px;background:var(--blue);display:flex;align-items:center;justify-content:center}
.copy{position:absolute;left:0;right:0;top:2800px;height:57px;background:var(--darker);color:#ccc;font-size:11px;display:flex;align-items:center;justify-content:center}
</style>
</head>
<body>

<header class="hero">
  <div class="hero-photo" role="img" aria-label="Photo of a warm open-plan living room with stone walls, timber beams, white armchairs and a spiral staircase"></div>
  <div class="topbar">
    <div class="wrap">
      <span class="contact"><span class="ic"><svg width="10" height="10" viewBox="0 0 24 24"><path fill="#333" d="M6.6 10.8a15 15 0 0 0 6.6 6.6l2.2-2.2c.3-.3.7-.4 1-.2 1.1.4 2.3.6 3.6.6.6 0 1 .4 1 1V20c0 .6-.4 1-1 1A17 17 0 0 1 3 4c0-.6.4-1 1-1h3.5c.6 0 1 .4 1 1 0 1.3.2 2.5.6 3.6.1.3 0 .7-.2 1z"/></svg></span>(555) 014 220 3861</span>
      <span class="contact"><span class="ic"><svg width="10" height="10" viewBox="0 0 24 24"><path fill="#333" d="M2 5h20v14H2z"/><path fill="none" stroke="#fff" stroke-width="2" d="M2 6l10 7 10-7"/></svg></span>info@example.com</span>
      <div class="social"><span></span><span></span><span></span><span></span></div>
    </div>
  </div>
  <nav class="nav">
    <div class="wrap">
      <div class="brand">NORTHGATE REALTY</div>
      <div class="menu">
        <a class="active">HOME</a><a>ABOUTUS</a><a>SERVICE</a><a>FOR SALSE</a><a>FOR RENT</a><a>CONTACT</a>
      </div>
    </div>
  </nav>
  <div class="hero-copy">
    <h1>GOLDEN MOONSOON</h1>
    <p>Lorem Ipsum is simply dummy text of the<br>printing and typesetting industry</p>
  </div>
  <div class="arrow prev"><svg width="40" height="10" viewBox="0 0 40 10"><path d="M40 5H2M6 1L2 5l4 4" stroke="#fff" fill="none"/></svg></div>
  <div class="arrow next"><svg width="40" height="10" viewBox="0 0 40 10"><path d="M0 5h38M34 1l4 4-4 4" stroke="#fff" fill="none"/></svg></div>
  <div class="dots"><span></span><span class="on"></span><span></span></div>
</header>

<section class="search">
  <div class="wrap grid">
    <div class="field"><label>Keyword</label><div class="box"></div></div>
    <div class="field"><label>Propert Type</label><div class="box">ALL TYPE<span>⌄</span></div></div>
    <div class="field"><label>Status</label><div class="box">ALL STATUS<span>⌄</span></div></div>
    <div class="field"><label>Location</label><div class="box"></div></div>
    <div class="field"><label>Bedroom</label><div class="box">ALL<span>⌄</span></div></div>
    <div class="field"><label>Bathroom</label><div class="box">ALL<span>⌄</span></div></div>
    <div class="field"><label>Price</label><div class="box">$27,0000.00<span>⌄</span></div></div>
    <div class="field"><div class="btn-search">Search Properties</div></div>
  </div>
</section>

<section class="about">
  <h2 class="title">ABOUT THE <b>NORTHGATE REALTY</b></h2>
  <div class="rule"></div>
  <div class="wrap about-body">
    <div class="collage">
      <div role="img" aria-label="Photo of a classic living room with chandelier" style="left:40px;top:0;width:190px;height:148px;background:linear-gradient(135deg,#e6b86a,#8a5a2c)"></div>
      <div role="img" aria-label="Photo of a modern white interior with glass walls" style="left:115px;top:60px;width:210px;height:170px;background:linear-gradient(135deg,#d8d8d8,#6a6a6a);transform:rotate(-3deg)"></div>
      <div role="img" aria-label="Photo of a bright sitting room with white sofas" style="left:2px;top:150px;width:170px;height:148px;background:linear-gradient(135deg,#e8dccb,#8c6b4c);transform:rotate(-2deg)"></div>
    </div>
    <div class="about-text">
      <p>Lorem ipsum dolor sit amet, consectetur adipiscing elit. Praesent quis tempus ex. Mauris commodo ex elementum ligula finibus, vel lobortis libero posuere. Donec condimentum erat sed imperdiet tempus. Cum sociis natoque penatibus et magnis dis parturient montes, nascetur ridiculus mus. Aenean gravida aliquam lacus quis convallis. Morbi non condimentum erat, eu ullamcorper felis. Donec id ligula ac nibh tristique ultrices. Quisque et eleifend est. Mauris vehicula, odio sed vulputate porttitor, nibh justo fringilla orci, sit amet interdum augue urna a magna. Fusce non dictum felis. Duis congue turpis non laoreet luctus.</p>
      <ul class="checks">
        <li><svg width="10" height="10" viewBox="0 0 10 10"><rect x=".5" y=".5" width="9" height="9" fill="none" stroke="#0355a3"/><path d="M2 5l2 2 4-4" fill="none" stroke="#0355a3"/></svg>Lorem ipsum dolor sit amet, consectetur adipiscing elit.</li>
        <li><svg width="10" height="10" viewBox="0 0 10 10"><rect x=".5" y=".5" width="9" height="9" fill="none" stroke="#0355a3"/><path d="M2 5l2 2 4-4" fill="none" stroke="#0355a3"/></svg>Duis gravida ipsum eget auctor mattis.</li>
        <li><svg width="10" height="10" viewBox="0 0 10 10"><rect x=".5" y=".5" width="9" height="9" fill="none" stroke="#0355a3"/><path d="M2 5l2 2 4-4" fill="none" stroke="#0355a3"/></svg>Curabitur dapibus sapien at orci tempor ultricies.</li>
        <li><svg width="10" height="10" viewBox="0 0 10 10"><rect x=".5" y=".5" width="9" height="9" fill="none" stroke="#0355a3"/><path d="M2 5l2 2 4-4" fill="none" stroke="#0355a3"/></svg>Quisque commodo est sed mi condimentum condimentum.</li>
      </ul>
    </div>
  </div>
</section>

<section class="services">
  <h2 class="title">OUR <b>SERVICES</b></h2>
  <div class="rule"></div>
  <div class="wrap svc-row">
    <div class="svc">
      <svg width="108" height="118" viewBox="0 0 108 118"><path d="M54 4a50 50 0 0 1 9 99l-9 12-9-12A50 50 0 0 1 54 4z" fill="#fff" stroke="#0355a3" stroke-width="3"/><path d="M32 52l22-18 22 18M38 48v22h32V48" fill="none" stroke="#0355a3" stroke-width="3"/><rect x="42" y="58" width="26" height="12" fill="#0355a3"/><text x="55" y="67" font-size="8" font-family="Open Sans,sans-serif" font-weight="700" fill="#fff" text-anchor="middle">RENT</text></svg>
      <h3>Renting Service</h3>
      <p>Consectetur adipisicing elit, sed do eiusmod tempor incididunt ut labore et dolore magna aliqua.</p>
      <span class="more">Read more ⟶</span>
    </div>
    <div class="svc">
      <svg width="108" height="118" viewBox="0 0 108 118"><path d="M54 4a50 50 0 0 1 9 99l-9 12-9-12A50 50 0 0 1 54 4z" fill="#fff" stroke="#0355a3" stroke-width="3"/><path d="M30 52l24-20 24 20" fill="none" stroke="#0355a3" stroke-width="3"/><path d="M36 48v24h36V48z" fill="#0355a3"/><circle cx="50" cy="62" r="6" fill="none" stroke="#fff" stroke-width="2"/><path d="M56 62h12M64 62v4" stroke="#fff" stroke-width="2"/></svg>
      <h3>Saling Service</h3>
      <p>Consectetur adipisicing elit, sed do eiusmod tempor incididunt ut labore et dolore magna aliqua.</p>
      <span class="more">Read more ⟶</span>
    </div>
    <div class="svc">
      <svg width="108" height="118" viewBox="0 0 108 118"><path d="M54 4a50 50 0 0 1 9 99l-9 12-9-12A50 50 0 0 1 54 4z" fill="#fff" stroke="#0355a3" stroke-width="3"/><path d="M38 48l16-14 16 14M42 45v14h24V45" fill="none" stroke="#0355a3" stroke-width="3"/><path d="M28 62c8 0 12 6 20 6h14c3 0 3 4 0 4H50M28 74h10l10 4 26-8" fill="none" stroke="#0355a3" stroke-width="3"/></svg>
      <h3>Property Management</h3>
      <p>Consectetur adipisicing elit, sed do eiusmod tempor incididunt ut labore et dolore magna aliqua.</p>
      <span class="more">Read more ⟶</span>
    </div>
    <div class="svc">
      <svg width="108" height="118" viewBox="0 0 108 118"><path d="M54 4a50 50 0 0 1 9 99l-9 12-9-12A50 50 0 0 1 54 4z" fill="#fff" stroke="#0355a3" stroke-width="3"/><rect x="34" y="58" width="7" height="14" fill="#0355a3"/><rect x="45" y="50" width="7" height="22" fill="#0355a3"/><rect x="56" y="54" width="7" height="18" fill="#0355a3"/><rect x="67" y="44" width="7" height="28" fill="#0355a3"/><path d="M32 52l14-12 10 6 16-12" fill="none" stroke="#0355a3" stroke-width="3"/><path d="M66 32h7v7" fill="none" stroke="#0355a3" stroke-width="3"/></svg>
      <h3>Free Market Analysis</h3>
      <p>Consectetur adipisicing elit, sed do eiusmod tempor incididunt ut labore et dolore magna aliqua.</p>
      <span class="more">Read more ⟶</span>
    </div>
  </div>
</section>

<section class="clients" role="img" aria-label="Dimmed photo of a dining room interior behind the client testimonial">
  <h2 class="title">CLIENT <b>SPEAK</b></h2>
  <div class="rule"></div>
  <p class="quote">Lorem ipsum dolor sit amet, consectetur adipisicing elit, sed do eiusmod tempor incididunt ut labore et dolore magna aliqua.<br>Ut enim ad minim veniam, quis nostrud exercitation ullamco laboris nisi ...</p>
  <div class="person">
    <div class="avatar" role="img" aria-label="Portrait of the client"></div>
    <div>Clara Venn<em>Family Residential</em></div>
  </div>
</section>

<section class="props">
  <h2 class="title">NEW <b>PROPERTIES</b></h2>
  <div class="rule"></div>
  <div class="wrap cards">
    <article class="card">
      <div class="photo" role="img" aria-label="Photo of a house with pool at sunset" style="background:linear-gradient(180deg,#e8a25a,#7a5a3a 60%,#3f6f8a)"><span class="price">$28,0000.00</span></div>
      <div class="info"><h4>Alder St, Los Angeles,EL 453018</h4><div class="tag">For Sale</div>
      <p>Duis aute irure dolor in repre in voluptate velit es sint cillumor dolore eu fugiatDuis aute irure dolor in repre in voluptate velit es sint cillumor dolore eu fugiat<br>Active Date: 2016/04/05 ~ 2017/04/30</p></div>
      <div class="meta">▢ 348<span class="r"><span>⊏ 4</span><span>⌂ 1</span></span></div>
    </article>
    <article class="card lift">
      <div class="photo" role="img" aria-label="Photo of a bright living room with white sofas" style="background:linear-gradient(160deg,#5a4a3a,#d8d0c4 55%,#8a7a68)"><span class="price">$42,0000.00</span></div>
      <div class="info"><h4>Birchwood St, Miami,SW 223190</h4><div class="tag">For Sale</div>
      <p>Duis aute irure dolor in repre in voluptate velit es sint cillumor dolore eu fugiatDuis aute irure dolor in repre in voluptate velit es sint cillumor dolore eu fugiat<br>Active Date: 2016/04/05 ~ 2017/04/30</p></div>
      <div class="meta">▢ 500<span class="r"><span>⊏ 4</span><span>⌂ 4</span></span></div>
    </article>
    <article class="card">
      <div class="photo" role="img" aria-label="Photo of a modern bedroom with white bed" style="background:linear-gradient(160deg,#3a4a66,#8a8c9a 55%,#3a2e2a)"><span class="price">$35,0000.00</span></div>
      <div class="info"><h4>Cedar Hill St, New Mexico,NM 5012</h4><div class="tag">For Sale</div>
      <p>Duis aute irure dolor in repre in voluptate velit es sint cillumor dolore eu fugiatDuis aute irure dolor in repre in voluptate velit es sint cillumor dolore eu fugiat<br>Active Date: 2016/04/05 ~ 2017/04/30</p></div>
      <div class="meta">▢ 400<span class="r"><span>⊏ 4</span><span>⌂ 3</span></span></div>
    </article>
  </div>
</section>

<footer class="footer">
  <div class="wrap">
    <div>
      <div class="brand">NORTHGATE REALTY</div>
      <p>Brighthome perspiciatis unde omnis iste natus error sit voluptatem accusantium doloremque laudantium aperiam.</p>
      <p style="margin-top:14px">Nemo enim ipsam voluptatem quia voluptas sit aspernatur.Lorem ipsum dolor sit amet, consectetur adipisicing elit, sed do eiusmod tempor incididunt</p>
    </div>
    <div class="fcontact">
      <h5>Contact</h5>
      <div><span class="ci"><svg width="10" height="10" viewBox="0 0 24 24"><path fill="#222" d="M6.6 10.8a15 15 0 0 0 6.6 6.6l2.2-2.2c.3-.3.7-.4 1-.2 1.1.4 2.3.6 3.6.6.6 0 1 .4 1 1V20c0 .6-.4 1-1 1A17 17 0 0 1 3 4c0-.6.4-1 1-1h3.5c.6 0 1 .4 1 1 0 1.3.2 2.5.6 3.6.1.3 0 .7-.2 1z"/></svg></span>1-800-123-4567</div>
      <div><span class="ci"><svg width="10" height="10" viewBox="0 0 24 24"><path fill="#222" d="M2 5h20v14H2z"/><path fill="none" stroke="#fff" stroke-width="2" d="M2 6l10 7 10-7"/></svg></span>info@example.com</div>
      <div><span class="ci"><svg width="10" height="10" viewBox="0 0 24 24"><path fill="#222" d="M12 2a7 7 0 0 0-7 7c0 5 7 13 7 13s7-8 7-13a7 7 0 0 0-7-7zm0 9.5A2.5 2.5 0 1 1 12 6.5a2.5 2.5 0 0 1 0 5z"/></svg></span>124, Lorem ipsum dolor sit<br>amet, consectetur adipisicing elit</div>
    </div>
    <div>
      <h5>Quick Links</h5>
      <ul class="links"><li>HOME</li><li>ABOUTUS</li><li>SERVICE</li><li>FOR SALSE</li><li>FOR RENT</li><li>CONTACT</li></ul>
    </div>
    <div>
      <h5>Newsletter</h5>
      <p>Lorem ipsum dolor sit amet, consectetur adipiscing elit. Curabitur tincidunt molestie neque. Integer laoreet ac nisi vel lobortis.</p>
      <div class="news-form"><span class="in">Email Id</span><span class="go"><svg width="13" height="13" viewBox="0 0 24 24"><path fill="#fff" d="M2 21l21-9L2 3v7l15 2-15 2z"/></svg></span></div>
    </div>
  </div>
</footer>
<div class="copy">Copyright © 2016 Northgate Realty. All rights reserved</div>

</body>
</html>
```